The Quiet Harbor Podcast Cover Art

I'm upgrading my podcast cover art to a new design. The show is called The Quiet Harbor and we interview guests who have gone through different challenges/adversities that we face in life. During the interview, we unpack how they've gotten past the adversity and how that insight might help others. I will link the show and old cover art. I will upload a new photo or two that can be used for the new cover art.

Look at previous cover for items that needed on the cover like Wavolo, larkpod etc.

Should also have a small caption that states
“UNTOLD STORIES OF EVERYDAY ADVERSITY & PERSEVERANCE”

Larkpod: https://open.larkpod.net/show/7QP2rTfaWmNcyHkVLbPDa9?si=zx4Kq-Rm81-Wd3TfBnvYqP

Target Market(s)

Podcast learning community

Industry/Entity Type

Podcast, Education

Colors
EB3D1F
EC4F4E
F09395
F8D3D4
FCEDEE

Requirements
Must have
• MR Logo, Colors are red, black and white.

```html
<!DOCTYPE html>
<html lang="en">
<head>
<meta charset="utf-8">
<title>The Quiet Harbor – Podcast Cover</title>
<link rel="stylesheet" href="https://fonts.googleapis.com/css2?family=Montserrat:ital,wght@0,200;0,600;0,700;1,700&family=Yellowtail&display=swap">
<style>
  :root {
    --red: #c41e24;
    --red-deep: #a3141c;
    --ink: #5a5a5a;
    --ink-soft: #7a7a7a;
    --paper: #ffffff;
    --photo-dark: #b9b9b9;
    --photo-mid: #d6d6d6;
  }
  html, body {
    margin: 0;
    padding: 0;
    width: 1200px;
    height: 1200px;
    overflow: hidden;
    background: var(--paper);
  }
  .cover {
    position: relative;
    width: 1200px;
    height: 1200px;
    background: var(--paper);
    overflow: hidden;
    font-family: "Montserrat", sans-serif;
  }
  .host-photo {
    position: absolute;
    left: 300px;
    top: 20px;
    width: 900px;
    height: 1180px;
    background:
      radial-gradient(ellipse 34% 30% at 62% 28%, var(--photo-dark) 0%, var(--photo-mid) 60%, rgba(255,255,255,0) 100%),
      radial-gradient(ellipse 70% 45% at 60% 85%, var(--photo-mid) 0%, #e6e6e6 55%, rgba(255,255,255,0) 100%);
  }
  .brand-mark {
    position: absolute;
    left: 50px;
    top: 48px;
    font-weight: 600;
    font-size: 62px;
    letter-spacing: -2px;
    color: var(--ink);
    line-height: 1;
  }
  .show-title {
    position: absolute;
    left: 108px;
    top: 280px;
    width: 460px;
    color: var(--red);
  }
  .show-monogram {
    display: block;
    font-weight: 700;
    font-size: 250px;
    line-height: 0.9;
    letter-spacing: -8px;
    color: var(--red);
  }
  .show-name-bold {
    display: block;
    margin-top: 14px;
    font-weight: 600;
    font-size: 104px;
    line-height: 1;
    letter-spacing: 1px;
  }
  .show-name-thin {
    display: block;
    font-weight: 200;
    font-size: 82px;
    line-height: 1.05;
    letter-spacing: 6px;
  }
  .show-host {
    display: flex;
    align-items: baseline;
    gap: 10px;
    margin-top: 2px;
  }
  .show-host-with {
    font-weight: 600;
    font-size: 18px;
    letter-spacing: 3px;
    text-transform: uppercase;
  }
  .show-host-name {
    font-family: "Yellowtail", cursive;
    font-size: 60px;
    line-height: 1;
    color: var(--red-deep);
  }
  .tagline {
    position: absolute;
    left: 112px;
    top: 1078px;
    margin: 0;
    font-weight: 700;
    font-style: italic;
    font-size: 25px;
    line-height: 1.65;
    letter-spacing: 3px;
    color: var(--ink);
    text-transform: uppercase;
  }
  .listen {
    position: absolute;
    left: 720px;
    top: 1048px;
    width: 400px;
  }
  .listen-label {
    display: block;
    text-align: center;
    font-weight: 600;
    font-size: 16px;
    letter-spacing: 11px;
    color: var(--ink);
    margin-bottom: 16px;
  }
  .platforms {
    display: flex;
    justify-content: space-between;
  }
  .platform {
    display: flex;
    align-items: center;
    gap: 10px;
    font-weight: 600;
    font-size: 34px;
    color: var(--ink);
  }
  .platform-dot {
    width: 40px;
    height: 40px;
    border-radius: 50%;
    background: var(--ink);
  }
</style>
</head>
<body>
  <main class="cover">
    <div class="host-photo" role="img" aria-label="Black-and-white portrait of the host smiling, wearing over-ear headphones, a light sweater and a chain necklace"></div>

    <div class="brand-mark">MR</div>

    <h1 class="show-title">
      <span class="show-monogram">QH</span>
      <span class="show-name-bold">QUIET</span>
      <span class="show-name-thin">HARBOR</span>
      <span class="show-host">
        <span class="show-host-with">with</span>
        <span class="show-host-name">Mara Rowe</span>
      </span>
    </h1>

    <p class="tagline">Untold stories of everyday<br>adversity &amp; perseverance</p>

    <div class="listen">
      <span class="listen-label">Listen on</span>
      <div class="platforms">
        <span class="platform"><span class="platform-dot"></span>Larkpod</span>
        <span class="platform"><span class="platform-dot"></span>Wavolo</span>
      </div>
    </div>
  </main>
</body>
</html>
```